CLICK HERE TO MEET ADVISOR ON VIDEO CALL

1. Our company (Talknest) is like PLINK but for online shoppers to Click the Graphic Link You Will Be Designing.
2. Copy for the link would invite online shopper to CLICK TO MEET OUR ADVISOR
3. If shopper clicks on the link, instantly they would meet our clients sales advisor on a 2-way video call. OUR BUSINESS IS IN ROUTING SHOPPERS TO ADVISORS ON VIDEO-SALES-CALLS
3. The Graphic you design would be placed on websites, emails, digital ads, etc.
4. In your graphic we want to INVITE THE SHOPPER TO CLICK, and SHOW WHAT A 2-WAY VIDEO CALL WOULD LOOK LIKE.
5. THERE IS 1 GRAPHIC ALREADY BEING USED IN CAR DEALERSHIPS. See: WWW.MARLOWAUTOS.NET and the current graphic will appear in lower left corner of their website home page.
6. We need a graphic for a white casually dressed male Real Estate Agent on a cell phone meeting with an African American mid 30s couple who are seeing the agent on their laptop

CLICK HERE TO MEET OUR ADVISOR

```html
<!DOCTYPE html>
<html lang="en">
<head>
<meta charset="utf-8">
<title>Talknest – Click Here To Meet Our Advisor</title>
<link href="https://fonts.googleapis.com/css2?family=Poppins:ital,wght@0,400;0,600;1,900&display=swap" rel="stylesheet">
<style>
  :root {
    --page-bg: #1f4389;
    --card-bg: #ffffff;
    --ink: #0b0b0b;
    --arc-blue: #4a7fe0;
    --arc-teal: #1fc0cf;
    --brand-blue: #3b6fe0;
    --photo-warm: #b9a48f;
    --photo-cool: #c9d3dd;
  }
  * { margin: 0; padding: 0; box-sizing: border-box; }
  html, body {
    width: 942px;
    height: 1200px;
    overflow: hidden;
    background: var(--page-bg);
    font-family: "Poppins", sans-serif;
  }
  .stage {
    position: relative;
    width: 942px;
    height: 1200px;
  }
  .advisor-link {
    position: absolute;
    left: 275px;
    top: 522px;
    width: 386px;
    height: 155px;
    background: var(--card-bg);
    border-radius: 16px;
    box-shadow: 0 6px 14px rgba(0, 0, 0, 0.28);
    overflow: hidden;
    display: block;
    text-decoration: none;
    color: var(--ink);
  }
  .call-art {
    position: absolute;
    inset: 0;
    width: 386px;
    height: 155px;
  }
  .cta {
    position: absolute;
    left: 174px;
    top: 24px;
    width: 200px;
    text-align: center;
  }
  .cta-headline {
    font-weight: 900;
    font-style: italic;
    font-size: 29px;
    line-height: 1;
    letter-spacing: 0.2px;
    white-space: nowrap;
  }
  .cta-sub {
    margin-top: 6px;
    font-weight: 400;
    font-size: 11.6px;
    letter-spacing: 0.2px;
    white-space: nowrap;
  }
  .brand {
    margin-top: 14px;
    display: flex;
    align-items: center;
    justify-content: center;
    gap: 6px;
  }
  .brand-dot {
    width: 14px;
    height: 14px;
    border-radius: 50%;
    background: var(--brand-blue);
  }
  .brand-name {
    font-weight: 600;
    font-size: 16px;
    color: var(--ink);
  }
</style>
</head>
<body>
  <main class="stage">
    <a class="advisor-link" href="#">
      <svg class="call-art" viewBox="0 0 386 155" aria-hidden="false">
        <defs>
          <linearGradient id="arcGradient" x1="0" y1="0" x2="0" y2="1">
            <stop offset="0" stop-color="var(--arc-blue)"/>
            <stop offset="1" stop-color="var(--arc-teal)"/>
          </linearGradient>
          <linearGradient id="couplePhoto" x1="0" y1="0" x2="1" y2="1">
            <stop offset="0" stop-color="#e8e4df"/>
            <stop offset="0.5" stop-color="var(--photo-warm)"/>
            <stop offset="1" stop-color="#6f625a"/>
          </linearGradient>
          <linearGradient id="advisorPhoto" x1="0" y1="0" x2="0" y2="1">
            <stop offset="0" stop-color="#e6dccd"/>
            <stop offset="1" stop-color="var(--photo-cool)"/>
          </linearGradient>
        </defs>

        <!-- sweeping divider band -->
        <path class="divider-arc" d="M103,0 Q172,58 175,155 L187,155 Q184,52 110,0 Z" fill="url(#arcGradient)"/>

        <!-- shopper bubble -->
        <g class="bubble bubble-shoppers">
          <path d="M18,78 L14,88 L28,83 Z" fill="#fff" stroke="#000" stroke-width="2" stroke-linejoin="round"/>
          <circle cx="50" cy="47" r="41" fill="url(#couplePhoto)" stroke="#000" stroke-width="2.2" role="img" aria-label="Photo of a couple smiling at their laptop during a video call"/>
        </g>

        <!-- advisor bubble -->
        <g class="bubble bubble-advisor">
          <path d="M150,134 L154,147 L140,142 Z" fill="#fff" stroke="#000" stroke-width="2" stroke-linejoin="round"/>
          <circle cx="120" cy="105" r="41" fill="url(#advisorPhoto)" stroke="#000" stroke-width="2.2" role="img" aria-label="Photo of a smiling sales advisor on the other end of the call"/>
        </g>

        <!-- pointer cursor -->
        <path class="cursor" d="M64,53 L64,92 L73,83 L80,99 L87,96 L80,80 L93,80 Z" fill="#fff" stroke="#000" stroke-width="2" stroke-linejoin="round"/>
      </svg>

      <div class="cta">
        <p class="cta-headline">CLICK HERE</p>
        <p class="cta-sub">TO MEET OUR ADVISOR</p>
        <div class="brand">
          <span class="brand-dot"></span>
          <span class="brand-name">Talknest</span>
        </div>
      </div>
    </a>
  </main>
</body>
</html>
```